Marlow Naturopathics business card design

Using the marlow logo designed, we would like that incorporated into a business card. A colour scheme which works with the logo and lists the following business details:

Dennis Marlow - Naturopath
Level 1, 58 Torvane Street
Wollongong NSW
(02) 4391 7084
www.dennismarlowhealth-example.com

We would also like space on the back of the card for next appointment times.

Target Market(s)

Anyone looking to improve their health

Industry/Entity Type

Business

Requirements
Must have
• Marlow Naturopathics logo, business details.
Nice to have
• Good colour schemes, attractive, eye-catching features that are easy to read.

```html
<!DOCTYPE html>
<html lang="en">
<head>
<meta charset="utf-8">
<title>Marlow Naturopathics – Business Card</title>
<link href="https://fonts.googleapis.com/css2?family=Cinzel:wght@600&family=Questrial&display=swap" rel="stylesheet">
<style>
  :root {
    --navy: #1b3f8f;
    --royal: #1565b8;
    --sky: #3aa6e0;
    --sky-pale: #d8effa;
    --warm: #fff4b8;
    --gold: #f5dc5a;
    --ink: #1a2a5c;
    --white: #ffffff;
  }
  html, body {
    margin: 0;
    padding: 0;
    overflow: hidden;
    background: #ffffff;
  }
  .card {
    position: relative;
    width: 1200px;
    height: 666px;
    overflow: hidden;
    background: var(--white);
  }
  .card__backdrop {
    position: absolute;
    inset: 0;
  }
  .brand {
    position: absolute;
    left: 60px;
    top: 130px;
    width: 400px;
    text-align: center;
  }
  .brand__dot {
    display: block;
    width: 150px;
    height: 150px;
    margin: 0 auto 34px;
    border-radius: 50%;
    background: var(--sky);
  }
  .brand__name {
    margin: 0;
    font-family: "Questrial", sans-serif;
    font-weight: 400;
    font-size: 36px;
    line-height: 1.2;
    color: var(--navy);
    white-space: nowrap;
  }
  .contact {
    position: absolute;
    right: 70px;
    top: 128px;
    text-align: right;
    color: var(--ink);
  }
  .contact__name {
    margin: 0;
    font-family: "Cinzel", serif;
    font-weight: 600;
    font-size: 44px;
    letter-spacing: 1px;
    color: var(--navy);
  }
  .contact__role {
    margin: 2px 0 0;
    font-family: "Questrial", sans-serif;
    font-size: 28px;
  }
  .contact__address {
    margin: 36px 0 0;
    font-family: "Questrial", sans-serif;
    font-style: normal;
    font-size: 30px;
    line-height: 1.42;
  }
  .website {
    position: absolute;
    right: 70px;
    bottom: 14px;
    margin: 0;
    font-family: "Questrial", sans-serif;
    font-size: 30px;
    letter-spacing: 2px;
    color: var(--white);
  }
</style>
</head>
<body>
<div class="card">
  <svg class="card__backdrop" width="1200" height="666" viewBox="0 0 1200 666" aria-hidden="true">
    <defs>
      <radialGradient id="warmGlow" cx="0.12" cy="0.35" r="0.6">
        <stop offset="0" stop-color="var(--warm)"/>
        <stop offset="0.55" stop-color="#fffbe6"/>
        <stop offset="1" stop-color="#ffffff"/>
      </radialGradient>
      <linearGradient id="skyField" x1="0" y1="0" x2="1" y2="0.3">
        <stop offset="0" stop-color="#ffffff"/>
        <stop offset="0.35" stop-color="var(--sky-pale)"/>
        <stop offset="1" stop-color="#6cc3ee"/>
      </linearGradient>
      <linearGradient id="bandFill" x1="0" y1="0" x2="1" y2="0">
        <stop offset="0" stop-color="var(--royal)"/>
        <stop offset="1" stop-color="var(--sky)"/>
      </linearGradient>
      <linearGradient id="bandLight" x1="0" y1="0" x2="1" y2="0">
        <stop offset="0" stop-color="#9ad6f3"/>
        <stop offset="1" stop-color="#cfeefc"/>
      </linearGradient>
    </defs>
    <rect width="1200" height="666" fill="url(#warmGlow)"/>
    <path class="sky-field" d="M660 0 C600 160 560 320 600 666 L1200 666 L1200 0 Z" fill="url(#skyField)"/>
    <path d="M610 0 C560 150 540 300 560 470" fill="none" stroke="var(--gold)" stroke-width="5" opacity="0.7"/>
    <path d="M640 0 C585 160 565 320 585 480" fill="none" stroke="#ffffff" stroke-width="12" opacity="0.9"/>
    <path class="wave-light" d="M0 568 C420 566 820 500 1200 420 L1200 666 L0 666 Z" fill="url(#bandLight)"/>
    <path d="M0 568 C420 566 820 500 1200 420" fill="none" stroke="var(--gold)" stroke-width="5"/>
    <path class="wave-band" d="M0 622 C440 616 840 560 1200 478 L1200 666 L0 666 Z" fill="url(#bandFill)"/>
    <path d="M0 622 C440 616 840 560 1200 478" fill="none" stroke="#ffffff" stroke-width="4" opacity="0.8"/>
  </svg>

  <div class="brand">
    <span class="brand__dot"></span>
    <p class="brand__name">Marlow Naturopathics</p>
  </div>

  <div class="contact">
    <h1 class="contact__name">Dennis Marlow</h1>
    <p class="contact__role">Naturopath</p>
    <address class="contact__address">
      Level 1, 58 Torvane Street<br>
      Wollongong NSW<br>
      (02) 4391 7084
    </address>
  </div>

  <p class="website">www.dennismarlowhealth-example.com</p>
</div>
</body>
</html>
```